Web Design Project

kestrel ridge works & services needs a new web design to go with its new logo design

we provide services such as instillation of fire sprinklers, fire hydrants , fire hose reels as well as fire extinguishers and fire blankets.

we can service these as well and also do the preventitave maintaince of these too.

we can do flow testing of sprinklers,hydrants & hosereels and test back flow prevention devices as well

old page is krws.com.au

```html
<!DOCTYPE html>
<html lang="en">
<head>
<meta charset="utf-8">
<title>Kestrel Ridge Works &amp; Services Pty Ltd</title>
<link href="https://fonts.googleapis.com/css2?family=Mulish:wght@700;800&family=Ubuntu:wght@400;500&family=Oswald:wght@500;600&family=Pinyon+Script&display=swap" rel="stylesheet">
<style>
:root{
  --bg-deep:#a8140c;
  --bg-mid:#c21d12;
  --panel:#b81c13;
  --content:#c7281f;
  --nav-top:#e9675c;
  --nav-bottom:#d63d31;
  --button:#dc4a3e;
  --footer:#dc5e55;
  --footer-edge:#c93b30;
  --ink-light:#fbeee6;
  --ink-cream:#efe4d2;
  --ink-dark:#3a0d08;
  --art-warm:#e8661f;
  --art-light:#f4b347;
}
*{margin:0;padding:0;box-sizing:border-box}
html,body{width:1200px;height:882px;overflow:hidden}
body{
  position:relative;
  background:
    radial-gradient(ellipse 500px 260px at 120px 120px,rgba(230,60,40,.35),transparent 70%),
    radial-gradient(ellipse 520px 300px at 1080px 760px,rgba(240,80,60,.3),transparent 70%),
    linear-gradient(135deg,var(--bg-mid),var(--bg-deep) 60%,#b5180f);
  font-family:"Mulish",sans-serif;
  color:var(--ink-light);
}
.page-panel{
  position:absolute;left:42px;top:36px;width:1116px;height:734px;
  background:rgba(190,30,20,.75);
}
.brand{
  position:absolute;left:0;width:1200px;top:104px;text-align:center;
  font-family:"Oswald",sans-serif;font-weight:600;color:var(--ink-cream);
}
.brand-mark{display:flex;align-items:center;justify-content:center;gap:18px;font-size:74px;line-height:1;letter-spacing:4px}
.brand-mark .dot{width:22px;height:22px;border-radius:50%;background:var(--ink-cream)}
.brand-name{font-size:21px;margin-top:38px;line-height:1}
.brand-tagline{font-size:14px;margin-top:4px;line-height:1}
.main-nav{
  position:absolute;left:86px;top:293px;width:1046px;height:48px;border-radius:8px;
  background:linear-gradient(var(--nav-top),var(--nav-bottom));
  display:flex;justify-content:center;align-items:center;gap:12px;padding-right:14px;
}
.main-nav a{
  display:block;width:92px;height:29px;border:1px solid #f6c9c2;background:var(--button);
  color:#fff;text-decoration:none;font-family:"Ubuntu",sans-serif;font-size:17px;
  text-align:center;line-height:27px;
}
.date-stamp{
  position:absolute;right:99px;top:351px;font-family:"Ubuntu",sans-serif;font-size:13px;color:var(--ink-light);
}
.welcome{
  position:absolute;left:180px;top:398px;width:445px;padding-bottom:2px;
  border-bottom:1px dashed var(--ink-light);white-space:nowrap;
  font-family:"Ubuntu",sans-serif;font-size:14px;font-weight:400;
}
.welcome .script{font-family:"Pinyon Script",cursive;font-size:28px;letter-spacing:2px;margin-right:6px}
.content-box{position:absolute;left:158px;top:435px;width:908px;height:320px;background:var(--content)}
.content-art{
  position:absolute;left:70px;top:50px;width:121px;height:172px;
  background:linear-gradient(180deg,var(--art-warm),var(--art-light));
}
.content-copy{
  position:absolute;left:235px;top:70px;width:638px;
  font-size:13px;font-weight:700;letter-spacing:.4px;line-height:18.6px;text-align:justify;hyphens:auto;
}
.content-copy p+p{margin-top:18.6px}
.site-footer{
  position:absolute;left:0;top:780px;width:1200px;height:88px;
  background:linear-gradient(var(--footer-edge) 0 15px,var(--footer) 15px);
  text-align:center;color:var(--ink-dark);font-size:14px;font-weight:800;
}
.footer-links{margin-top:30px;word-spacing:2px}
.footer-links a{color:var(--ink-dark);text-decoration:none;margin:0 14px}
.copyright{margin-top:6px;word-spacing:2px}
</style>
</head>
<body>
  <div class="page-panel"></div>

  <header class="brand">
    <div class="brand-mark"><span>KRWS</span><span class="dot"></span></div>
    <div class="brand-name">KESTREL RIDGE WORKS &amp; SERVICES PTY LTD</div>
    <div class="brand-tagline">YOUR BEST DEFENCE AGAINST FIRE</div>
  </header>

  <nav class="main-nav">
    <a href="#">Home</a>
    <a href="#">Service</a>
    <a href="#">Testing</a>
    <a href="#">Products</a>
    <a href="#">FAQ'S</a>
  </nav>

  <div class="date-stamp">Wednesday, October 26, 2011 05:37 PM</div>

  <h1 class="welcome"><span class="script">Welcome to</span>Kestrel Ridge Works &amp; Services Pty Ltd</h1>

  <section class="content-box">
    <div class="content-art" role="img" aria-label="Illustration of a fire flame"></div>
    <div class="content-copy">
      <p>At Kestrel Ridge we believe that no matter how large or small your business is we can help you with the design, installation and the maintenance of your system to the standard which it was designed to.</p>
      <p>Kestrel Ridge is a fire protection company situated on the Central Coast of NSW and is currently servicing the Sydney, Central Coast and Hunter areas, We are always looking for new clients who are not happy with there current service providers and are looking for a Competitive priced alternative. Kestrel Ridge will come to your site and assess your fire service assets and provide a full quotation on a 12 month service contract.</p>
    </div>
  </section>

  <footer class="site-footer">
    <div class="footer-links"><a href="#">Contact Us</a>/<a href="#">Request Quote</a>/<a href="#">Button</a></div>
    <div class="copyright">Copyright 2010 KRWS.COM.AU All Rights Reserved.</div>
  </footer>
</body>
</html>
```